We need a design for our retail display and for our stockist's retail display.
Our product is fresh corn tortillas. These can be used to make tacos, quesadillas, tortilla chips and tostadas.
We want the table talker to use our brand style (see our website) and show the tortillas versatility.
verdel-foods.co.uk
It should also have a space for our stockists to write in a blank space under the heading "Our fresh tortillas are delivered every....[blank space]"
The table talker should be 75mm tall x 150mm wide. This will also have a 25mm self adhesive flap at the top which can be blank or the same colour as the background.
Please feel free to use any files from our website as well as illustrations attached.
Customers in high end shops and delis
food and drink

```html
<!DOCTYPE html>
<html lang="en">
<head>
<meta charset="utf-8">
<title>Verdel Foods Table Talker</title>
<link href="https://fonts.googleapis.com/css2?family=Oswald:wght@300;400;600;700&family=Yellowtail&display=swap" rel="stylesheet">
<style>
  :root {
    --stage: #e4e1de;
    --navy: #1f3150;
    --navy-deep: #1a2943;
    --yellow: #fdd600;
    --gold: #d9c766;
    --white: #ffffff;
    --ink: #14120c;
    --illustration: #c9a800;
  }
  * { margin: 0; padding: 0; box-sizing: border-box; }
  html, body { width: 1200px; height: 1043px; overflow: hidden; background: var(--stage); }
  .talker {
    position: absolute; left: 40px; top: 148px;
    width: 1120px; height: 747px;
    background: var(--navy);
    overflow: hidden;
    font-family: "Oswald", sans-serif;
  }
  .flap { position: absolute; left: 0; top: 0; width: 100%; height: 170px; background: var(--navy-deep); }
  .headline {
    position: absolute; left: 0; top: 200px; width: 100%;
    text-align: center; text-transform: uppercase;
    font-weight: 700; font-size: 86px; line-height: 1; letter-spacing: 1px;
    color: var(--white);
  }
  .headline .accent { color: var(--yellow); }
  .subhead {
    position: absolute; left: 0; top: 300px; width: 100%;
    text-align: center; font-size: 70px; line-height: 1; font-weight: 700;
    text-transform: uppercase; color: var(--gold);
  }
  .subhead .script {
    font-family: "Yellowtail", cursive; text-transform: none; font-weight: 400;
    color: var(--yellow); font-size: 72px; margin-right: 10px;
  }
  .delivery {
    position: absolute; left: 0; top: 420px; width: 100%;
    text-align: center; font-weight: 300; font-size: 34px; color: var(--white);
    text-transform: uppercase; letter-spacing: 0.5px;
  }
  .write-in {
    position: absolute; left: 290px; top: 512px; width: 540px; height: 2px;
    background: var(--white);
  }
  .border-pattern {
    position: absolute; left: 0; top: 540px; width: 100%; height: 34px;
    background: linear-gradient(var(--navy-deep), #2a3a52);
  }
  .base-band {
    position: absolute; left: 0; top: 574px; width: 100%; height: 173px;
    background: var(--yellow);
  }
  .brand-seal {
    position: absolute; left: 28px; top: 8px; width: 156px; height: 156px;
    border-radius: 50%; background: var(--navy);
    display: flex; align-items: center; justify-content: center; text-align: center;
    color: var(--yellow); font-weight: 600; font-size: 26px; line-height: 1.1;
    text-transform: uppercase; letter-spacing: 1px;
  }
  .dishes {
    position: absolute; left: 210px; top: 12px; width: 890px;
    display: flex; justify-content: space-between;
  }
  .dish { width: 150px; text-align: center; }
  .dish-art {
    width: 120px; height: 100px; margin: 0 auto 10px;
    border-radius: 18px;
    background: radial-gradient(circle, var(--illustration) 0%, var(--yellow) 80%);
  }
  .dish-name {
    font-weight: 600; font-size: 21px; color: var(--ink); text-transform: uppercase;
  }
</style>
</head>
<body>
  <section class="talker">
    <div class="flap"></div>
    <h1 class="headline">Fresh Corn <span class="accent">Tortillas</span></h1>
    <p class="subhead"><span class="script">and other</span>Mexican Ingredients</p>
    <p class="delivery">Our fresh tortillas are delivered every</p>
    <div class="write-in"></div>
    <div class="border-pattern" role="img" aria-label="Decorative geometric border pattern"></div>
    <div class="base-band">
      <div class="brand-seal">Verdel<br>Foods</div>
      <div class="dishes">
        <div class="dish"><div class="dish-art" role="img" aria-label="Drawing of tacos"></div><span class="dish-name">Tacos</span></div>
        <div class="dish"><div class="dish-art" role="img" aria-label="Drawing of a quesadilla"></div><span class="dish-name">Quesadilla</span></div>
        <div class="dish"><div class="dish-art" role="img" aria-label="Drawing of tortilla chips"></div><span class="dish-name">Tortilla Chips</span></div>
        <div class="dish"><div class="dish-art" role="img" aria-label="Drawing of taquitos"></div><span class="dish-name">Taquitos</span></div>
        <div class="dish"><div class="dish-art" role="img" aria-label="Drawing of a tostada"></div><span class="dish-name">Tostada</span></div>
      </div>
    </div>
  </section>
</body>
</html>
```